Velora Company website for beauty pre & post natal products

i need to have a company website for my new start up company Velora. Velora means woman in latin. My website url is www.velora-mums.example, i have no contents yet. Velora is focus on selling pre and post natal beauty products e.g.: maternity belt, post natal girdles, maternity bra, etc.. products that beautify woman before and after maternity. I would like the website to potray beauty and yet confident woman. i have attached the sample of the product.
Updates

hi creative designers, I'm looking for your creativity that best to portray my company website, a local company based in Singapore that focus on selling beauty pre and post natal products to beautify motherhood and all women out there

Target Market(s)

Women (age 24-40), mother, career woman, etc

Industry/Entity Type

It Company

Number of Pages Required

5+ page

Font styles to use
Serif
Sans Serif

Requirements
Must have
• - Home page
• (highlights of products, company, beauty elegant women with small children, etc)
• - About Us
• Velora is founded in 2015 in Singapore by a proud mommy of 2 sons. During maternity period which before and after pregnancy, it is extremely crucial for woman to give extra care for herself and her body from the effect of pregnancy due to physical and hormonal changes.
• - Products
• - Client's testimonials
• - Contact Us
• - Inquiry Form
Nice to have
• Professional, yet elegant and appealing to women nowadays. It should show level of trust and credibility just from entering the website.
Should not have
• BIG NO to dark colors, gloomy colors or animations.

```html
<!DOCTYPE html>
<html lang="en">
<head>
<meta charset="utf-8">
<title>Velora – Pre and Post Natal Products</title>
<link href="https://fonts.googleapis.com/css2?family=Raleway:wght@300;400&family=Great+Vibes&family=Varela+Round&family=Open+Sans:wght@400;700&family=Arimo:wght@400;700&display=swap" rel="stylesheet">
<style>
  :root {
    --brand-red: #b3282b;
    --brand-red-deep: #a52226;
    --blush: #f3b6b0;
    --blush-soft: #f7cfca;
    --label-red: #d0655a;
    --price-red: #c0302e;
    --heading-red: #b5262b;
    --body-text: #3a2a2a;
    --white: #ffffff;
    --role-gold: #fde9b0;
    --frame: #d9d9d9;
  }
  * { box-sizing: border-box; margin: 0; padding: 0; }
  html, body { width: 1200px; height: 2620px; overflow: hidden; background: var(--white); }
  body { position: relative; font-family: "Varela Round", sans-serif; color: var(--body-text); }
  .abs { position: absolute; }

  .page-shapes { position: absolute; left: 0; top: 0; }

  .site-logo {
    position: absolute; left: 520px; top: 38px;
    font-family: "Raleway", sans-serif; font-weight: 400;
    font-size: 50px; color: var(--white); letter-spacing: 1px;
  }
  .main-nav { position: absolute; top: 123px; left: 0; width: 1200px; }
  .main-nav a {
    position: absolute; font-family: "Raleway", sans-serif; font-weight: 400;
    font-size: 19px; color: var(--white); text-decoration: none; white-space: nowrap;
  }
  .hero-title {
    position: absolute; left: 722px; top: 240px; width: 460px;
    font-family: "Raleway", sans-serif; font-weight: 300;
    font-size: 43px; line-height: 52px; color: var(--white); letter-spacing: 0.5px;
  }

  .script-heading {
    position: absolute; font-family: "Great Vibes", cursive; font-weight: 400;
    color: var(--heading-red); font-size: 60px; line-height: 1; white-space: nowrap;
  }
  .welcome-photo {
    position: absolute; left: 80px; top: 900px; width: 365px; height: 360px;
    border-radius: 45% 45% 20% 20%;
    background: radial-gradient(ellipse at 50% 45%, #e8d2c4 0%, #c9b3a6 45%, rgba(255,255,255,0) 72%);
  }
  .welcome-text {
    position: absolute; left: 493px; top: 1020px; width: 630px;
    font-size: 16.5px; line-height: 20px; color: var(--body-text);
  }
  .read-more {
    position: absolute; left: 513px; top: 1148px;
    font-size: 16px; color: var(--heading-red); text-decoration: none;
  }

  .product-card { position: absolute; width: 204px; }
  .product-frame {
    width: 204px; height: 183px; border: 1px solid var(--frame); background: var(--white);
    padding: 2px;
  }
  .product-photo { width: 100%; height: 100%; }
  .product-name {
    margin-top: 18px; font-family: "Open Sans", sans-serif; font-size: 13.5px;
    color: var(--label-red); text-transform: uppercase; white-space: nowrap;
  }
  .product-price {
    margin-top: 0px; font-family: "Open Sans", sans-serif; font-weight: 700;
    font-size: 19.5px; color: var(--price-red);
  }
  .tone-beige { background: linear-gradient(180deg, #e9d6c6 0%, #e4c7b2 55%, #f1e4da 100%); }
  .tone-rose { background: linear-gradient(180deg, #f0e2da 0%, #a9786c 35%, #b08478 70%, #e9d2c6 100%); }
  .tone-cream { background: linear-gradient(180deg, #b98562 0%, #efe0c8 35%, #ecdcc2 75%, #c99a78 100%); }
  .tone-mocha { background: linear-gradient(180deg, #c69d88 0%, #9f7565 40%, #a97f6f 80%, #d7b4a3 100%); }
  .tone-cocoa { background: linear-gradient(180deg, #e9cfc0 0%, #e3c2b0 30%, #4a2a20 45%, #3f231b 65%, #e2c3b4 80%, #efd9cd 100%); }

  .testimonial-heading { color: var(--white); }
  .testimonial { position: absolute; width: 330px; }
  .avatar {
    position: absolute; width: 152px; height: 152px; border-radius: 50%;
    border: 4px solid var(--white);
  }
  .avatar-a { background: radial-gradient(circle at 50% 45%, #e8c7b8, #9d6a5d 60%, #f2e2d8 100%); }
  .avatar-b { background: radial-gradient(circle at 50% 45%, #e6c1ad, #8a5846 60%, #ece7e6 100%); }
  .avatar-c { background: radial-gradient(circle at 50% 45%, #e9cfc3, #2f1f1d 60%, #f3f1f1 100%); }
  .quote-mark {
    position: absolute; font-family: "Open Sans", sans-serif; font-weight: 700;
    font-size: 30px; color: var(--white); line-height: 1;
  }
  .quote-text {
    position: absolute; font-family: "Open Sans", sans-serif; font-size: 16.5px;
    line-height: 20px; color: var(--white); width: 340px;
  }
  .quote-name {
    position: absolute; font-family: "Arimo", sans-serif; font-weight: 700;
    font-size: 18.5px; color: var(--white); white-space: nowrap;
  }
  .quote-role {
    position: absolute; font-family: "Arimo", sans-serif; font-size: 13.5px;
    color: var(--role-gold); white-space: nowrap;
  }

  .site-footer {
    position: absolute; left: 42px; top: 2571px;
    font-family: "Arimo", sans-serif; font-size: 14px; color: var(--white);
  }
</style>
</head>
<body>

<svg class="page-shapes" width="1200" height="2620" viewBox="0 0 1200 2620" aria-hidden="true">
  <path d="M0,790 H1200 V915 C1000,872 800,848 560,850 Z" fill="var(--blush)"/>
  <path d="M0,0 H1200 V828 C900,815 620,860 330,852 C170,848 70,836 0,822 Z" fill="var(--brand-red)"/>
  <path d="M0,740 C200,770 420,800 700,815 C900,822 1050,824 1200,828 V840 C900,830 620,862 330,855 C170,851 70,840 0,828 Z" fill="var(--brand-red-deep)"/>
  <path d="M0,1915 C260,1890 520,1885 800,1905 C960,1918 1080,1945 1200,1968 V2620 H0 Z" fill="var(--blush)"/>
  <path d="M0,2530 C260,2498 600,2552 900,2540 C1020,2535 1110,2520 1200,2508 V2620 H0 Z" fill="var(--brand-red)"/>
</svg>

<svg class="abs" style="left:0;top:0" width="1200" height="840" viewBox="0 0 1200 840" role="img" aria-label="Smiling expectant mother in a flowing pink satin dress">
  <defs>
    <linearGradient id="heroTone" x1="0" y1="0" x2="0.6" y2="1">
      <stop offset="0" stop-color="#ffffff"/>
      <stop offset="0.35" stop-color="#f6dcdf"/>
      <stop offset="0.7" stop-color="#ec7fa0"/>
      <stop offset="1" stop-color="#f3b7c8"/>
    </linearGradient>
  </defs>
  <path d="M0,0 H470 C440,150 450,430 560,560 C680,700 900,790 1140,830 C820,810 320,790 0,760 Z" fill="url(#heroTone)"/>
</svg>

<div class="site-logo">Velora</div>
<nav class="main-nav">
  <a style="left:519px" href="#">HOME</a>
  <a style="left:601px" href="#">ABOUT US</a>
  <a style="left:721px" href="#">PRODUCTS</a>
  <a style="left:842px" href="#">TESTIMONIALS</a>
  <a style="left:993px" href="#">CONTACT US</a>
</nav>
<h1 class="hero-title">PRE AND POST NATAL PRODUCTS FOR BEAUTIFUL AND CONFIDENT WOMAN</h1>

<div class="welcome-photo" role="img" aria-label="Mother sitting with her two young daughters"></div>
<h2 class="script-heading" style="left:450px;top:932px">Welcome to Velora</h2>
<p class="welcome-text">Lorem ipsum dolor sit amet conse ctetur adipisicing elit, sed do eiusmod tempor incididunt ut labore. Lorem ipsum dolor sit amet conse ctetur adipisicing elit, sed do eiusmod tempor incididunt ut labore et dolore magna aliqua. Ut enim ad minim veniam, quis nostrud exercitation ullamco laboris nisi ut aliquip ex ea commodo consequat.</p>
<a class="read-more" href="#">read more</a>

<h2 class="script-heading" style="right:30px;top:1218px">Our Products</h2>

<div class="product-card" style="left:35px;top:1313px"><div class="product-frame"><div class="product-photo tone-beige" role="img" aria-label="Nude post natal high-waist girdle"></div></div><div class="product-name">Post Girdle</div><div class="product-price">$30.28</div></div>
<div class="product-card" style="left:267px;top:1313px"><div class="product-frame"><div class="product-photo tone-rose" role="img" aria-label="Rose pre natal waist cincher"></div></div><div class="product-name">Pre Girdle</div><div class="product-price">$26.51</div></div>
<div class="product-card" style="left:500px;top:1313px"><div class="product-frame"><div class="product-photo tone-cream" role="img" aria-label="Cream full body shaper"></div></div><div class="product-name">RB Golf Cap</div><div class="product-price">$20.28</div></div>
<div class="product-card" style="left:732px;top:1313px"><div class="product-frame"><div class="product-photo tone-mocha" role="img" aria-label="Mocha bodysuit shaper"></div></div><div class="product-name">Black Red Classic Cap</div><div class="product-price">$53.68</div></div>
<div class="product-card" style="left:966px;top:1313px"><div class="product-frame"><div class="product-photo tone-cocoa" role="img" aria-label="Dark brown maternity belly belt"></div></div><div class="product-name">Green Green Dillinger</div><div class="product-price">$20.28</div></div>

<div class="product-card" style="left:35px;top:1605px"><div class="product-frame"><div class="product-photo tone-beige" role="img" aria-label="Nude post natal high-waist girdle"></div></div><div class="product-name">Post Girdle</div><div class="product-price">$30.28</div></div>
<div class="product-card" style="left:267px;top:1605px"><div class="product-frame"><div class="product-photo tone-rose" role="img" aria-label="Rose pre natal waist cincher"></div></div><div class="product-name">Pre Girdle</div><div class="product-price">$26.51</div></div>
<div class="product-card" style="left:500px;top:1605px"><div class="product-frame"><div class="product-photo tone-cream" role="img" aria-label="Cream full body shaper"></div></div><div class="product-name">RB Golf Cap</div><div class="product-price">$20.28</div></div>
<div class="product-card" style="left:732px;top:1605px"><div class="product-frame"><div class="product-photo tone-mocha" role="img" aria-label="Mocha bodysuit shaper"></div></div><div class="product-name">Black Red Classic Cap</div><div class="product-price">$53.68</div></div>
<div class="product-card" style="left:966px;top:1605px"><div class="product-frame"><div class="product-photo tone-cocoa" role="img" aria-label="Dark brown maternity belly belt"></div></div><div class="product-name">Green Green Dillinger</div><div class="product-price">$20.28</div></div>

<h2 class="script-heading testimonial-heading" style="left:472px;top:1968px">Testimonials</h2>

<div class="avatar avatar-a" style="left:134px;top:2094px" role="img" aria-label="Portrait of client Owen Pritchard"></div>
<div class="quote-mark" style="left:55px;top:2258px">&ldquo;</div>
<p class="quote-text" style="left:55px;top:2278px">Vel illum dolore eu feugiat nulla facilisis at vero eros et accumsan et iusto dignissim qui blandit praesent lupt zril delenit augue duis dolore te feugait nulla facilisi.</p>
<div class="quote-name" style="left:55px;top:2396px">Owen Pritchard</div>
<div class="quote-role" style="left:55px;top:2422px">Accounting &nbsp;Officer</div>

<div class="avatar avatar-b" style="left:513px;top:2094px" role="img" aria-label="Portrait of client Rachel Jordane"></div>
<div class="quote-mark" style="left:438px;top:2258px">&ldquo;</div>
<p class="quote-text" style="left:438px;top:2278px">Typi non habent claritatem insitam est us legentis in iis qui facit eorum claritatem. Investigationes demonstraverunt lectores legere me lius quod ii legunt saepius.</p>
<div class="quote-name" style="left:438px;top:2375px">Rachel Jordane</div>
<div class="quote-role" style="left:438px;top:2401px">Accounting &nbsp;Officer</div>

<div class="avatar avatar-c" style="left:920px;top:2094px" role="img" aria-label="Portrait of client Clara Menzies"></div>
<div class="quote-mark" style="left:833px;top:2258px">&ldquo;</div>
<p class="quote-text" style="left:833px;top:2278px">Claritas est etiam processus dynamicus sequitur mutationem consuetudium lectorum. Mirum est notare quam littera gothica, quam nunc pumus parum clam, anteposuerit litterarum formas.</p>
<div class="quote-name" style="left:833px;top:2396px">Clara Menzies</div>
<div class="quote-role" style="left:833px;top:2422px">President, CEO of Brightlane</div>

<footer class="site-footer">&copy; Velora 2015. All rights reserved. Privacy Policy</footer>

</body>
</html>
```